Lanterns for Paws Christmas Cards

We want to send this to all our donors and partners. Hoping for a design that says hope and compassion and shows the benefit of their support. We offer essential pet programs to the vulnerable such as a pet food bank. safekeeping, youth and senior education, vet care assistance. Thank you!

```html
<!DOCTYPE html>
<html lang="en">
<head>
<meta charset="utf-8">
<title>Lanterns for Paws — Stationery</title>
<link href="https://fonts.googleapis.com/css2?family=Poppins:wght@400;500;600;700&display=swap" rel="stylesheet">
<style>
:root{
  --bg:#e7e8ea;
  --paper:#ffffff;
  --ink:#2b2a2c;
  --red:#e3242b;
  --red-deep:#c32f33;
  --grey:#6d6d70;
  --shadow:0 10px 22px rgba(0,0,0,.35);
}
*{box-sizing:border-box;margin:0;padding:0}
html,body{width:1200px;height:1200px;overflow:hidden;background:var(--bg);font-family:"Poppins",sans-serif;color:var(--ink)}
.canvas{position:relative;width:1200px;height:1200px}
.piece{position:absolute;background:var(--paper);box-shadow:var(--shadow);overflow:hidden}
.abs{position:absolute}
.wave{position:absolute;left:0;bottom:0;width:100%}
.brand{position:absolute;display:flex;flex-direction:column;align-items:center;gap:4px}
.brand-dot{border-radius:50%;background:var(--red)}
.brand-name{color:var(--red);font-weight:700;white-space:nowrap;line-height:1}
.name{color:var(--red);font-weight:600;line-height:1.1}
.tagline{font-weight:500;line-height:1.2}
.contact{position:absolute;list-style:none;color:#fff}
.contact li{display:flex;align-items:center;gap:6px}
.contact svg{flex:none}
.offer-title{font-weight:600;text-align:center}
.offer-list{list-style:none;display:flex;justify-content:center}
.offer-list li{display:flex;align-items:center;gap:5px}
.offer-list li::before{content:"";width:3px;height:3px;border-radius:50%;background:currentColor}
.socials{position:absolute;display:flex}
.socials span{border-radius:50%;background:var(--red)}
.lorem{font-size:4.6px;line-height:11.6px;color:#555}
.label{color:var(--red);font-weight:500}
</style>
</head>
<body>
<svg width="0" height="0" style="position:absolute">
  <defs>
    <symbol id="swoosh" viewBox="0 0 516 145" preserveAspectRatio="none">
      <path d="M0,10 C140,-12 300,20 400,46 C450,58 490,60 516,56 L516,145 L0,145Z" fill="#c32f33"/>
      <path d="M0,18 C140,0 300,28 400,56 L516,66 L516,145 L0,145Z" fill="#2b2a2c"/>
      <path d="M250,40 C330,64 420,86 516,80 L516,92 C420,98 320,76 250,44Z" fill="#e3242b"/>
    </symbol>
    <symbol id="ico" viewBox="0 0 10 10">
      <circle cx="5" cy="5" r="5" fill="#e3242b"/>
      <circle cx="5" cy="5" r="1.8" fill="#fff"/>
    </symbol>
  </defs>
</svg>

<main class="canvas">

  <!-- Business card front -->
  <section class="piece card-front" style="left:70px;top:47px;width:320px;height:183px">
    <p class="name abs" style="left:23px;top:40px;font-size:13px">Mara Ellison</p>
    <p class="tagline abs" style="left:23px;top:56px;font-size:9px">Tagline Goes Here</p>
    <div class="brand" style="left:205px;top:32px;width:100px">
      <span class="brand-dot" style="width:34px;height:34px"></span>
      <span class="brand-name" style="font-size:10px">Lanterns for Paws</span>
    </div>
    <svg class="wave" style="height:90px"><use href="#swoosh" width="100%" height="100%"/></svg>
    <ul class="contact" style="left:23px;top:112px;font-size:7px;line-height:12.5px">
      <li><svg width="8" height="8"><use href="#ico"/></svg>+00 555 0142 870</li>
      <li><svg width="8" height="8"><use href="#ico"/></svg>hello@lanternpaws.org</li>
      <li><svg width="8" height="8"><use href="#ico"/></svg>www.lanternpaws.org</li>
      <li style="margin-top:2px"><svg width="8" height="8"><use href="#ico"/></svg>12 Harbor Lane 40213 Brookfield</li>
    </ul>
  </section>

  <!-- Compliment slip -->
  <section class="piece slip" style="left:497px;top:47px;width:616px;height:231px">
    <div class="socials" style="left:28px;top:28px;gap:6px">
      <span style="width:15px;height:15px"></span><span style="width:15px;height:15px"></span>
      <span style="width:15px;height:15px"></span><span style="width:15px;height:15px"></span>
    </div>
    <p class="name abs" style="left:244px;top:56px;font-size:20px">Mara Ellison</p>
    <p class="tagline abs" style="left:244px;top:81px;font-size:14px">Tagline Goes Here</p>
    <div class="brand" style="left:470px;top:30px;width:130px">
      <span class="brand-dot" style="width:50px;height:50px"></span>
      <span class="brand-name" style="font-size:13px">Lanterns for Paws</span>
    </div>
    <svg class="wave" style="height:136px"><use href="#swoosh" width="100%" height="100%"/></svg>
    <ul class="contact" style="left:28px;top:138px;font-size:9.5px;line-height:15.5px">
      <li><svg width="10" height="10"><use href="#ico"/></svg>+00 555 0142 870</li>
      <li><svg width="10" height="10"><use href="#ico"/></svg>hello@lanternpaws.org</li>
      <li><svg width="10" height="10"><use href="#ico"/></svg>www.lanternpaws.org</li>
      <li style="margin-top:3px"><svg width="10" height="10"><use href="#ico"/></svg>12 Harbor Lane 40213 Brookfield</li>
    </ul>
  </section>

  <!-- Business card back -->
  <section class="piece card-back" style="left:70px;top:305px;width:320px;height:183px">
    <div class="brand" style="left:85px;top:24px;width:150px">
      <span class="brand-dot" style="width:46px;height:46px"></span>
      <span class="brand-name" style="font-size:13px;margin-top:4px">Lanterns for Paws</span>
    </div>
    <div class="abs offer-band" style="left:0;top:134px;width:320px;height:49px;background:var(--ink);color:#fff;padding-top:6px">
      <p class="offer-title" style="font-size:8px">We offer</p>
      <ul class="offer-list" style="font-size:5.6px;gap:10px;margin-top:6px">
        <li>pet food bank</li><li>safekeeping</li><li>youth and senior education</li><li>vet care assistance</li>
      </ul>
    </div>
  </section>

  <!-- Envelope -->
  <section class="piece envelope" style="left:485px;top:325px;width:368px;height:184px">
    <svg class="abs" style="left:0;top:0" width="368" height="66" viewBox="0 0 368 66">
      <path d="M0,0 H368 L352,46 Q346,64 326,64 H42 Q22,64 16,46 Z" fill="var(--red-deep)"/>
    </svg>
    <p class="name abs" style="left:22px;top:73px;font-size:9.5px">Mara Ellison</p>
    <p class="tagline abs" style="left:22px;top:85px;font-size:6.5px">Tagline Goes Here</p>
    <span class="brand-dot abs" style="left:298px;top:70px;width:31px;height:31px"></span>
    <svg class="wave" style="height:84px"><use href="#swoosh" width="100%" height="100%"/></svg>
    <ul class="contact" style="left:22px;top:122px;font-size:5.4px;line-height:10px">
      <li><svg width="6" height="6"><use href="#ico"/></svg>+00 555 0142 870</li>
      <li><svg width="6" height="6"><use href="#ico"/></svg>hello@lanternpaws.org</li>
      <li><svg width="6" height="6"><use href="#ico"/></svg>www.lanternpaws.org</li>
      <li style="margin-top:1px"><svg width="6" height="6"><use href="#ico"/></svg>12 Harbor Lane 40213 Brookfield</li>
    </ul>
  </section>

  <!-- Insert card -->
  <section class="piece insert" style="left:745px;top:422px;width:368px;height:183px">
    <div class="brand" style="left:134px;top:20px;width:100px;opacity:.15">
      <span class="brand-dot" style="width:36px;height:36px"></span>
      <span class="brand-name" style="font-size:10px;margin-top:14px">Lanterns for Paws</span>
    </div>
    <p class="offer-title abs" style="left:0;top:99px;width:100%;font-size:9.5px">We offer</p>
    <ul class="offer-list abs" style="left:0;top:116px;width:100%;font-size:7px;gap:14px">
      <li>pet food bank</li><li>safekeeping</li><li>youth and senior education</li><li>vet care assistance</li>
    </ul>
    <div class="brand" style="left:12px;top:132px;width:50px;gap:2px">
      <span class="brand-dot" style="width:14px;height:14px"></span>
      <span class="brand-name" style="font-size:4.5px">Lanterns for Paws</span>
    </div>
  </section>

  <!-- Letterhead -->
  <section class="piece letterhead" style="left:76px;top:619px;width:349px;height:494px">
    <div class="brand" style="left:20px;top:26px;width:95px">
      <span class="brand-dot" style="width:32px;height:32px"></span>
      <span class="brand-name" style="font-size:9px;margin-top:10px">Lanterns for Paws</span>
    </div>
    <div class="socials" style="left:262px;top:28px;gap:6px">
      <span style="width:11px;height:11px"></span><span style="width:11px;height:11px"></span>
      <span style="width:11px;height:11px"></span><span style="width:11px;height:11px"></span>
    </div>
    <div class="abs recipient" style="left:26px;top:123px;width:90px">
      <p class="label" style="font-size:8px">To</p>
      <p class="label" style="font-size:7px;margin-top:3px">Mara Ellison</p>
      <p style="font-size:3.8px;line-height:6.5px;margin-top:3px">48 Willow Row,<br>Brookfield, BR 40213</p>
      <p class="label" style="font-size:6px;margin-top:18px">Date:</p>
      <p style="font-size:6px;margin-top:2px;letter-spacing:.4px">00-00-0000</p>
      <div style="font-size:3.8px;line-height:5.2px;margin-top:33px">
        <p class="label">Phone</p><p>+1555 01428</p>
        <p class="label" style="margin-top:7px">Email</p><p>mail@lanternpaws.org</p>
        <p class="label" style="margin-top:7px">Website</p><p>www.lanternpaws.org</p>
        <p class="label" style="margin-top:7px">Address</p><p>Lorem ipsum dolor sit amet</p>
      </div>
    </div>
    <span class="abs" style="left:117px;top:124px;width:.6px;height:176px;background:#999"></span>
    <div class="abs letter-body" style="left:151px;top:123px;width:178px">
      <p style="font-size:8.5px;font-weight:600"><span style="color:var(--red)">Dear</span> Client</p>
      <p class="lorem" style="margin-top:8px">Lorem ipsum dolor sit amet, consectetuer adipiscing elit, sed diam nonummy nibh euismod tincidunt ut laoreet dolore magna aliquam erat volutpat. Ut wisi enim ad minim veniam, quis nostrud exerci tation ullamcorper suscipit lobortis nisl ut aliquip ex ea commodo consequat. Duis autem vel eum iriure dolor in hendrerit in vulputate</p>
      <p class="lorem" style="margin-top:10px">Lorem ipsum dolor sit amet, consectetuer adipiscing elit, sed diam nonummy nibh euismod tincidunt ut laoreet dolore magna aliquam erat volutpat. Ut wisi enim ad minim veniam, quis nostrud exerci tation ullamcorper suscipit lobortis nisl ut aliquip ex ea commodo</p>
      <p class="lorem" style="margin-top:10px">Lorem ipsum dolor sit amet, consectetuer adipiscing elit, sed diam nonummy nibh euismod tincidunt ut laoreet dolore magna aliquam erat volutpat. Ut wisi enim ad minim veniam</p>
      <p style="font-size:6.8px;font-weight:600;margin-top:14px">Owen <span style="color:var(--red)">Hartley</span></p>
      <p style="font-size:4.6px;border-bottom:.6px solid #999;width:55px;padding-bottom:2px">Manager</p>
      <div role="img" aria-label="Handwritten signature" style="width:90px;height:34px;margin-top:6px;background:linear-gradient(90deg,#f1f1f1,#e2e2e2)"></div>
      <p style="font-size:8px;font-weight:500;margin-top:6px;margin-left:6px">We offer</p>
    </div>
    <svg class="wave" style="height:82px"><use href="#swoosh" width="100%" height="100%"/></svg>
    <div class="abs terms" style="left:26px;top:431px;width:100px;color:#fff">
      <p style="font-size:7px;font-weight:500">Terms &amp; Conditions</p>
      <p style="font-size:4px;line-height:7.5px;margin-top:5px;color:#ddd">Lorem ipsum dolor sit amet, consectetuer adipiscing elit, sed diam nonummy nibh euismod tincidunt ut laoreet dolore</p>
    </div>
  </section>

  <!-- Christmas card front -->
  <section class="piece card-cover" style="left:497px;top:714px;width:283px;height:399px">
    <div class="brand" style="left:86px;top:28px;width:111px">
      <span class="brand-dot" style="width:34px;height:34px"></span>
      <span class="brand-name" style="font-size:10px;margin-top:10px">Lanterns for Paws</span>
    </div>
    <h1 class="abs headline" style="left:0;top:170px;width:100%;text-align:center;font-size:22px;line-height:25px;color:#000">
      <span style="font-weight:700">Made possible</span><br>
      <span style="font-weight:500">by your <span style="color:var(--red);font-weight:600">kindness</span></span>
    </h1>
    <span class="abs" style="left:50px;top:226px;width:183px;height:1.2px;background:linear-gradient(90deg,transparent,var(--red) 20%,var(--red) 80%,transparent)"></span>
    <svg class="wave" style="height:82px"><use href="#swoosh" width="100%" height="100%"/></svg>
  </section>

  <!-- Christmas card inside -->
  <section class="piece card-thanks" style="left:828px;top:714px;width:285px;height:399px">
    <div class="abs frame" style="left:23px;top:22px;width:240px;height:353px;border:2.5px solid var(--ink)"></div>
    <div class="abs" role="img" aria-label="Scroll ornament along the top edge" style="left:28px;top:24px;width:230px;height:14px;background:linear-gradient(90deg,#dcdcdc,#bdbdbd,#dcdcdc)"></div>
    <div class="abs" role="img" aria-label="Scroll ornament along the bottom edge" style="left:28px;top:358px;width:230px;height:14px;background:linear-gradient(90deg,#dcdcdc,#bdbdbd,#dcdcdc)"></div>
    <span class="abs" style="left:32px;top:112px;width:3px;height:112px;background:repeating-linear-gradient(180deg,var(--red) 0 8px,transparent 8px 11px)"></span>
    <span class="abs" style="left:252px;top:172px;width:3px;height:120px;background:repeating-linear-gradient(180deg,var(--red) 0 8px,transparent 8px 11px)"></span>
    <div class="brand" style="left:92px;top:56px;width:101px">
      <span class="brand-dot" style="width:34px;height:34px"></span>
      <span class="brand-name" style="font-size:9.5px;margin-top:10px">Lanterns for Paws</span>
    </div>
    <div class="abs" role="img" aria-label="Hand-lettered thank you in red script" style="left:58px;top:146px;width:172px;height:58px;background:linear-gradient(90deg,#f6d6d7,#efc0c2)"></div>
    <p class="abs" style="left:80px;top:212px;font-size:17px;font-weight:600;line-height:18px">For Giving<br>Hope</p>
    <div class="abs" style="left:54px;top:264px;width:178px;height:44px;border:.8px solid var(--ink);border-radius:2px;display:flex;align-items:center;justify-content:center;text-align:center;font-size:8px;line-height:12.5px">
      Lorem ipsum dolor sit amet,<br>consectetuer adipiscing elit, sed diam<br>nonummy nibh euismod tincidunt ut
    </div>
  </section>

</main>
</body>
</html>
```